Redesign of my Homepage - Online resource for anyone to learn American Sign Language

I would like to have a new homepage design http://www.SignPathora.com . My business is a website for anyone to learn American Sign Language. There are over 300 video lessons, with each lesson having 20 vocabulary words, retention exercises, 16,000 video dictionary etc. It is a very extensive site. It is a self paced website. If you need a log in to see what customers see, please let me know. I would like to keep the same color scheme. I want the website to look modern and clean. I want a fresh look! I want something that is easy to navigate, attracts customers, and easy to follow. I would like the final design to communicate that my website is for anyone to learn how to sign with this incredible program.

Target Market(s)

Students taking American Sign Language, Parents with Deaf children, future interpreters for the deaf, co-workers of the Deaf. Also, schools that offer American Sign Language (online schools, homeschools, etc. ).

Industry/Entity Type

Business

Number of Pages Required

1 page

Requirements
Must have
• My project must be very clean and clear. I want my homepage to show that this is a program for people to learn how American Sign Language.
Nice to have
• Not sure. Surprise me.

```html
<!DOCTYPE html>
<html lang="en">
<head>
<meta charset="utf-8">
<title>SignPathora – Learn American Sign Language</title>
<link href="https://fonts.googleapis.com/css2?family=Oswald:wght@400;500&family=Open+Sans:wght@400;600;700&display=swap" rel="stylesheet">
<style>
:root{
  --cream:#fbf1dc;
  --green:#5aa832;
  --orange:#f7941d;
  --teal:#0a8f93;
  --amber:#ef7d00;
  --olive:#8b9b00;
  --mint:#2fae84;
  --footer:#e7e7e7;
  --ink:#333;
  --white:#fff;
}
*{box-sizing:border-box;margin:0;padding:0}
html,body{width:938px;height:1200px;overflow:hidden;background:var(--white);font-family:"Open Sans",sans-serif;color:var(--ink)}
.page{position:relative;width:938px;height:1200px}

.brand-panel{position:absolute;left:0;top:0;width:389px;height:99px;background:var(--cream)}
.brand{position:absolute;left:58px;top:32px;display:flex;align-items:center;gap:8px}
.brand-mark{width:16px;height:16px;background:var(--green)}
.brand-name{font-family:"Open Sans",sans-serif;font-weight:700;font-size:26px;color:#222;line-height:34px}

.login-panel{position:absolute;left:389px;top:0;width:549px;height:99px;background:var(--green)}
.login-panel::before{content:"";position:absolute;left:0;top:38px;border-left:12px solid var(--cream);border-top:11px solid transparent;border-bottom:11px solid transparent}
.login-title{position:absolute;left:39px;top:24px;font-weight:600;font-size:15px;color:var(--white);letter-spacing:.2px}
.field{position:absolute;top:51px;height:29px;background:var(--white);font-size:10px;color:#555;padding:8px 10px}
.field.user{left:37px;width:164px}
.field.pass{left:204px;width:157px}
.field svg{position:absolute;right:8px;top:6px}
.signin{position:absolute;left:369px;top:51px;width:70px;height:29px;background:var(--orange);color:var(--white);font-size:11px;font-weight:700;text-align:center;line-height:29px}
.forgot{position:absolute;left:445px;top:53px;font-size:10px;line-height:12px;color:var(--white)}

.hero{position:absolute;left:0;top:99px;width:938px;height:431px;background:linear-gradient(100deg,#c9c2b6 0%,#8f98a3 35%,#b49a8d 60%,#6a7d52 100%)}
.nav{position:absolute;left:0;top:99px;width:938px;height:35px;background:rgba(40,40,40,.82);display:flex;align-items:center;padding-left:61px}
.nav a{font-weight:600;font-size:12px;color:var(--white);text-decoration:none;padding:0 11px;height:26px;line-height:26px;white-space:nowrap}
.nav a.active{background:var(--green);padding:0 12px}
.nav .caret{font-size:8px;margin-left:3px}
.hero-title{position:absolute;left:0;top:190px;width:938px;text-align:center;font-family:"Oswald",sans-serif;font-weight:500;font-size:50px;color:var(--white);letter-spacing:-.5px;line-height:1}
.btn-outline{display:flex;align-items:center;justify-content:center;gap:8px;border:2px solid var(--white);color:var(--white);font-size:12px;height:27px;width:112px}
.hero .btn-outline{position:absolute;left:414px;top:267px}
.dots{position:absolute;left:448px;top:405px;display:flex;gap:5px}
.dots span{width:11px;height:11px;border-radius:50%;background:var(--white)}
.dots span.on{border:2px solid var(--green)}

.social{position:absolute;left:0;top:226px;width:37px}
.social span{display:block;height:34px;margin-bottom:2px;background:var(--white);border:2px solid var(--green);border-left:none;position:relative}
.social span::after{content:"";position:absolute;left:11px;top:10px;width:10px;height:10px;border-radius:50%;background:var(--green)}

.card{position:absolute;top:574px;width:260px;height:468px;overflow:hidden;color:var(--white);text-align:center}
.card.community{left:58px;background:var(--teal)}
.card.parents{left:339px;background:var(--amber)}
.card.students{left:621px;background:var(--olive)}
.card .photo{position:absolute;left:0;top:0;width:260px;height:250px;clip-path:polygon(0 0,100% 0,100% 194px,0 250px)}
.community .photo{background:linear-gradient(180deg,#e8e8e8,#8c8c8c)}
.parents .photo{background:linear-gradient(160deg,#d9d6cf,#6b6458)}
.students .photo{background:linear-gradient(160deg,#546a5c,#c49a6e)}
.badge{position:absolute;left:98px;top:198px;width:64px;height:64px;border-radius:50%;border:3px solid var(--white);display:flex;align-items:center;justify-content:center}
.community .badge{background:var(--teal)}
.parents .badge{background:var(--amber)}
.students .badge{background:var(--olive)}
.card .kicker{position:absolute;top:276px;width:100%;font-family:"Oswald",sans-serif;font-size:15px;line-height:1}
.card .title{position:absolute;top:296px;width:100%;font-family:"Oswald",sans-serif;font-weight:500;font-size:27px;line-height:1}
.card .blurb{position:absolute;top:346px;left:20px;width:220px;font-size:12.5px;line-height:16px}
.card .btn-outline{position:absolute;left:74px;top:403px}

.cta{position:absolute;left:382px;top:1079px;width:174px;height:42px;background:var(--mint);border-bottom:3px solid #1f7d5e;color:var(--white);font-weight:700;font-size:14px;text-align:center;line-height:40px;letter-spacing:.3px}

.footer{position:absolute;left:0;top:1158px;width:938px;height:42px;background:var(--footer);font-size:12px;color:#555}
.footer-links{position:absolute;left:57px;top:13px;display:flex;gap:9px}
.copyright{position:absolute;right:57px;top:14px}
</style>
</head>
<body>
<div class="page">
  <header>
    <div class="brand-panel">
      <div class="brand"><span class="brand-mark"></span><span class="brand-name">SignPathora</span></div>
    </div>
    <div class="login-panel">
      <div class="login-title">HOW TO LEARN ASL THROUGH VIDEO LESSONS ONLINE</div>
      <div class="field user">User Name
        <svg width="16" height="17" viewBox="0 0 16 17"><circle cx="8" cy="5" r="4" fill="none" stroke="#aaa"/><path d="M1 16c0-4 3-6 7-6s7 2 7 6z" fill="none" stroke="#aaa"/></svg>
      </div>
      <div class="field pass">Password
        <svg width="14" height="17" viewBox="0 0 14 17"><path d="M3 7V5a4 4 0 0 1 8 0v2" fill="none" stroke="#aaa"/><rect x="1" y="7" width="12" height="9" rx="2" fill="none" stroke="#aaa"/></svg>
      </div>
      <div class="signin">Sign In</div>
      <div class="forgot">Forgot<br>Password</div>
    </div>
  </header>

  <section class="hero" role="img" aria-label="Photo of a boy and a woman smiling while watching a lesson on a laptop">
    <div class="hero-title">ASL TUTOR ONLINE</div>
    <div class="btn-outline">LEARN MORE
      <svg width="14" height="10" viewBox="0 0 14 10"><path d="M1 5h12M9 1l4 4-4 4" fill="none" stroke="#fff" stroke-width="1.6"/></svg></div>
    <div class="dots"><span class="on"></span><span></span><span></span></div>
  </section>

  <nav class="nav">
    <a class="active">HOME</a>
    <a>HOW IT WORKS<span class="caret">▼</span></a>
    <a>GIFT CERTIFICATES</a>
    <a>TRY IT FREE</a>
    <a>BUY NOW</a>
    <a>CONTACT US<span class="caret">▼</span></a>
    <a>GROUP RATE FORM</a>
    <a>TEACHER'S GUIDE</a>
  </nav>

  <div class="social" aria-label="Social links">
    <span></span><span></span><span></span><span></span><span></span><span></span>
  </div>

  <article class="card community">
    <div class="photo" role="img" aria-label="Group photo of people from many professions"></div>
    <div class="badge"><svg width="36" height="28" viewBox="0 0 36 28" fill="#fff"><circle cx="8" cy="8" r="4"/><circle cx="28" cy="8" r="4"/><circle cx="18" cy="6" r="5"/><rect x="2" y="14" width="12" height="12" rx="4"/><rect x="22" y="14" width="12" height="12" rx="4"/><rect x="11" y="13" width="14" height="15" rx="5"/></svg></div>
    <div class="kicker">LEARNING</div>
    <div class="title">COMMUNITY</div>
    <p class="blurb">Anyone that has a passion to learn American Sign Language (ASL)</p>
    <div class="btn-outline">LEARN MORE <svg width="14" height="10" viewBox="0 0 14 10"><path d="M1 5h12M9 1l4 4-4 4" fill="none" stroke="#fff" stroke-width="1.6"/></svg></div>
  </article>

  <article class="card parents">
    <div class="photo" role="img" aria-label="Photo of parents with their young daughter"></div>
    <div class="badge"><svg width="32" height="32" viewBox="0 0 32 32" fill="#fff"><circle cx="9" cy="6" r="4"/><circle cx="23" cy="6" r="4"/><circle cx="16" cy="15" r="3"/><rect x="4" y="11" width="10" height="19" rx="3"/><rect x="18" y="11" width="10" height="19" rx="3"/><rect x="13" y="19" width="6" height="10" rx="2"/></svg></div>
    <div class="kicker">HEARING PARENTS OF DEAF CHILDREN</div>
    <div class="title">PARENTS</div>
    <p class="blurb">Learn to communicate more effectively with your child</p>
    <div class="btn-outline">LEARN MORE <svg width="14" height="10" viewBox="0 0 14 10"><path d="M1 5h12M9 1l4 4-4 4" fill="none" stroke="#fff" stroke-width="1.6"/></svg></div>
  </article>

  <article class="card students">
    <div class="photo" role="img" aria-label="Photo of a classroom with a teacher and pupils raising hands"></div>
    <div class="badge"><svg width="34" height="32" viewBox="0 0 34 32" fill="#fff"><rect x="12" y="2" width="20" height="13" fill="none" stroke="#fff" stroke-width="2"/><circle cx="7" cy="6" r="3"/><rect x="4" y="10" width="6" height="10" rx="2"/><circle cx="8" cy="24" r="2.5"/><circle cx="17" cy="24" r="2.5"/><circle cx="26" cy="24" r="2.5"/><rect x="5" y="27" width="6" height="5" rx="2"/><rect x="14" y="27" width="6" height="5" rx="2"/><rect x="23" y="27" width="6" height="5" rx="2"/></svg></div>
    <div class="kicker">DEAF AND HARD OF HEARING</div>
    <div class="title">STUDENTS</div>
    <p class="blurb">Learn to tackle the challenges you faced in the classroom</p>
    <div class="btn-outline">LEARN MORE <svg width="14" height="10" viewBox="0 0 14 10"><path d="M1 5h12M9 1l4 4-4 4" fill="none" stroke="#fff" stroke-width="1.6"/></svg></div>
  </article>

  <div class="cta">TRY IT FREE</div>

  <footer class="footer">
    <div class="footer-links"><span>Contact Us</span><span>Our Mission</span><span>Terms &amp; Conditions</span></div>
    <div class="copyright">© 2017 SignPathora.&nbsp; All Rights Reserved | 1485238575.2956s</div>
  </footer>
</div>
</body>
</html>
```